Need somewhat upscale, eye catching honey jar label to make our product stand out on store shelves.

We need front and back labels for a honey jar. Files "Honey Jar Front Label 2" & "Honey Jar Back Label 2" show what I have come up with.

Files "Honey Jar Front Label 2". I did this as an example. It shows the information that needs to be included on the front label. The picture was taken by my daughter. The information and picture can be rearranged, enlarged, reduced, cropped, etc. as you see fit.

Files "Honey Jar Back Label 2". I did this one to play with the wording to get the information to fit. It explains how I keep bees. It can be worded differently as long as all the information is included.

I know nothing about good use of color, borders, backgrounds, font style and size, etc. so please excuse my plain presentations. I admire and respect your creative abilities very much.

Since my method of keeping bees involves a lot of travel time and expense, as mentioned in files "Honey Jar Back Label 2" I will try to price my honey a little higher than the competition so please design accordingly with that in mind.

We think we want to use a traditional jar with stick on labels like Marlow's jar seen in file Marlow's Jar. However, feel free to use a different jar as long as the honey can be easily scooped out with a spoon and does not have to be poured out. I know that eliminates a lot of fancy jars but that's what my customers want. Jar size should be 12 ounces which will hold a little more than 1 pound of honey.

Hanging labels are also acceptable therefore jar shapes that will not accept a stick on label can also be used. An example is a Honeypot Jar.

And of course we like Hexagon Jars which are 6 sided like the cells in honeycomb.

Please stick to glass jars that are readily available. No custom shaped jars for now.

Marlow's jar is clear glass and the metal lid is a light golden color.

It's probably a good idea for the shape of the labels to match the shape of the bottle like I marked in black on Marlow's Jar. Being wider in the middle should allow the back label to be shorter than my example seen in files "Honey Jar Back Label 2". I think front and back labels should be the same size.

The shape of the area marked in black around Marlow's label measures 1-1/4 (1.25) inches across the top, 2-1/4 (2.25) inches across the middle, 2 inches across the bottom and 3-1/2 (3.5) inches tall from top to bottom.

Target Market(s)

People wanting local honey that is not processed in any way.
People that are willing to pay a little more for honey from bees that are kept in a sustainable way (see the story in files 2 & 17) without the use of harsh chemicals.

Industry/Entity Type

Travel

Font styles to use
Serif
Decorative
Script

Requirements
Must have
• See my lengthy project description, file "Honey Jar Front Label 2" and file "Honey Jar Back Label 2". All of the info. therein is very important.
• Somewhat upscale, eye catching appearance that makes the product stand out on store shelves and suggests that the honey inside is quality, unprocessed truly local honey.
Nice to have
• If bullets are used they can look like a skep (type of beehive). I have included an example in a file.
• Swirly dashed line coming off the s in lin-Wren's with a honeybee at the end of it. See files for examples.
• Swirly dashed line coming off the i in wildflower making the shape of a heart with a honeybee at the end of it hovering over the o in wildflower and the o looks like a flower. See files for examples.

```html
<!DOCTYPE html>
<html lang="en">
<head>
<meta charset="utf-8">
<title>lin-Wren's Local Honey – Jar Labels</title>
<link rel="stylesheet" href="https://fonts.googleapis.com/css2?family=Cinzel:wght@500&family=Marcellus&family=Questrial&display=swap">
<style>
  :root {
    --page: #ffffff;
    --label-black: #141414;
    --label-sheen: #2e2e2e;
    --rim-yellow: #f6cf2a;
    --gold: #e9a92a;
    --gold-light: #f3cf7a;
    --gold-dark: #9c6a1c;
    --honey-orange: #f5b000;
    --comb-yellow: #f8d23a;
    --comb-amber: #eaa11a;
    --text-white: #ffffff;
  }
  * { box-sizing: border-box; margin: 0; padding: 0; }
  html, body { width: 1200px; height: 810px; overflow: hidden; background: var(--page); }
  .canvas { position: relative; width: 1200px; height: 810px; }
  .label-shapes { position: absolute; inset: 0; }
  .label { position: absolute; top: 0; width: 510px; height: 810px; color: var(--text-white); font-family: "Questrial", sans-serif; }
  .label--front { left: 67px; }
  .label--back { left: 622px; }
  .block { position: absolute; left: 0; width: 510px; text-align: center; z-index: 2; }

  /* Front */
  .rating-stars { position: absolute; left: 190px; top: 57px; width: 100px; height: 12px; border-radius: 6px;
    background: linear-gradient(90deg, var(--gold-dark), var(--gold-light), var(--gold-dark)); }
  .premium { top: 84px; left: -10px; font-family: "Cinzel", serif; font-size: 40px; letter-spacing: 2px;
    color: var(--gold-light); }
  .brand-name { top: 150px; left: -10px; font-size: 48px; color: var(--gold); }
  .title-plate { position: absolute; left: 66px; top: 213px; width: 354px; height: 75px; border-radius: 12px;
    border: 4px solid var(--gold); background: linear-gradient(180deg, #3a3a3a, #0c0c0c 60%, #1e1e1e);
    font-family: "Marcellus", serif; font-size: 46px; line-height: 66px; text-align: center; }
  .claims { top: 308px; left: -10px; font-size: 20px; line-height: 27.5px; }
  .tagline { top: 398px; left: -10px; font-size: 27px; color: var(--honey-orange); }
  .bee-trail { position: absolute; left: 118px; top: 445px; width: 280px; height: 110px; border-radius: 55px;
    background: radial-gradient(ellipse at 80% 40%, rgba(248,210,58,0.45), rgba(255,255,255,0.08) 60%, transparent 80%); }
  .variety { top: 562px; left: -10px; font-family: "Marcellus", serif; font-size: 46px; }
  .net-weight { top: 620px; left: -10px; font-size: 20px; }
  .comb { position: absolute; z-index: 1; clip-path: polygon(25% 0, 75% 0, 100% 50%, 75% 100%, 25% 100%, 0 50%);
    background: linear-gradient(135deg, var(--comb-yellow), var(--comb-amber)); }
  .comb--left { left: 48px; top: 652px; width: 130px; height: 100px; }
  .comb--right { left: 300px; top: 652px; width: 130px; height: 100px; }

  /* Back */
  .origin-city { top: 56px; font-size: 22px; }
  .origin-title { top: 88px; font-size: 24px; }
  .counties { top: 118px; font-size: 18px; line-height: 25px; }
  .practice-title { top: 197px; font-family: "Marcellus", serif; font-size: 28px; }
  .practice-text { top: 230px; font-size: 14px; line-height: 19.3px; white-space: nowrap; }
  .nutrition-title { top: 484px; font-size: 20px; }
  .nutrition-intro { top: 510px; font-size: 16px; line-height: 22.5px; }
  .nutrition-table { position: absolute; left: 144px; top: 598px; border-collapse: collapse; font-size: 15.5px; }
  .nutrition-table td { height: 22.4px; padding: 0; }
  .nutrition-table .nutrient { width: 120px; }
  .nutrition-table .amount { width: 46px; text-align: right; padding-right: 20px; }
  .nutrition-table .amount--left { text-align: left; }
  .nutrition-table .sub { padding-left: 5px; }
  .bee-mark { position: absolute; left: 378px; top: 585px; width: 70px; height: 80px; border-radius: 50%;
    background: radial-gradient(circle at 55% 60%, rgba(248,210,58,0.6), rgba(255,255,255,0.12) 65%, transparent 80%); }
</style>
</head>
<body>
<div class="canvas">
  <svg class="label-shapes" width="1200" height="810" viewBox="0 0 1200 810" aria-hidden="true">
    <defs>
      <linearGradient id="labelFill" x1="0" y1="0" x2="1" y2="0.3">
        <stop offset="0" stop-color="#101010"/>
        <stop offset="0.45" stop-color="#1a1a1a"/>
        <stop offset="0.55" stop-color="#2e2e2e"/>
        <stop offset="0.7" stop-color="#161616"/>
        <stop offset="1" stop-color="#0e0e0e"/>
      </linearGradient>
      <path id="labelOutline" d="M115 45 Q322 2 530 45 C575 200 580 560 548 755 Q322 805 97 755 C65 560 70 200 115 45 Z"/>
    </defs>
    <use href="#labelOutline" fill="url(#labelFill)" stroke="var(--rim-yellow)" stroke-width="7"/>
    <use href="#labelOutline" transform="translate(555 0)" fill="url(#labelFill)" stroke="var(--rim-yellow)" stroke-width="7"/>
  </svg>

  <section class="label label--front">
    <div class="rating-stars" role="img" aria-label="Row of five gold stars"></div>
    <div class="block premium">PREMIUM</div>
    <div class="block brand-name">lin-Wren's</div>
    <div class="title-plate">Local Honey</div>
    <div class="block claims">100% Pure, Raw, Unaltered<br>Never Heated<br>Strained Not Micro-filtered</div>
    <div class="block tagline">She works hard for the honey</div>
    <div class="bee-trail" role="img" aria-label="Honeybee flying at the end of a dashed heart-shaped trail"></div>
    <div class="block variety">Wildflower</div>
    <div class="block net-weight">Net Weight 16 oz /454g</div>
    <div class="comb comb--left" role="img" aria-label="Honeycomb cells"></div>
    <div class="comb comb--right" role="img" aria-label="Honeycomb cells"></div>
  </section>

  <section class="label label--back">
    <div class="block origin-city">Atlanta’s</div>
    <div class="block origin-title">Local Honey</div>
    <div class="block counties">Bees kept in Cobb, Cherokee, DeKalb,<br>Douglas, Forsyth, Gwinnett,<br>Hall &amp; Jackson Counties.</div>
    <div class="block practice-title">Sustainable Beekeeping</div>
    <p class="block practice-text">* Partnering with local farmers and landowners we<br>spread our bees out over many square miles, keeping fewer<br>bees at more locations. Although much more time consuming<br>and expensive, it allows the pollinators to benefit more of the<br>environment and ensures them more abundant natural food.<br>This eliminates the need to feed cane sugar or high fructose corn<br>syrups which results in healthier bees and purer honey, not<br>contaminated with syrup.<br>* We will never sacrifice the health of the bees or the<br>quality of their honey for profit. Never!<br>* We sell honey from our bees only.<br>* Do not feed to infants under 1 year old.<br>http://lin-Wrens.com</p>
    <div class="block nutrition-title">Nutrition Facts</div>
    <div class="block nutrition-intro">Serv. Size 1 Tbsp (21g) / Serv. Per Container 21<br>Percent Daily Values (DV)<br>are based on a 2,000 calorie diet.<br>Amount Per Serving</div>
    <table class="nutrition-table">
      <tr><td class="nutrient">Calories</td><td class="amount amount--left">64</td><td></td></tr>
      <tr><td class="nutrient">Total Fat</td><td class="amount">0g</td><td>0% DV</td></tr>
      <tr><td class="nutrient">Sodium</td><td class="amount">0mg</td><td>0% DV</td></tr>
      <tr><td class="nutrient">Total Carbs</td><td class="amount">17g</td><td>6% DV</td></tr>
      <tr><td class="nutrient sub">Sugars</td><td class="amount">16g</td><td></td></tr>
      <tr><td class="nutrient">Protein</td><td class="amount">0g</td><td>0% DV</td></tr>
    </table>
    <div class="bee-mark" role="img" aria-label="Small honeybee illustration"></div>
  </section>
</div>
</body>
</html>
```